Bref créative
Bright Path Fund - Not for Profit - Stationary and Business Cards
Professional
Dale Meridew
President and Chairman of the Board
20573 Lindale Avenue #238
Helotes, Texas 78154
dale.meridew@brightpathfund.org
www.brightpathfund.org
Implement colors from the logo theme.
incorporate the logo into the design.
Bright Path Fund logo - AI format

```html
<!DOCTYPE html>
<html lang="en">
<head>
<meta charset="utf-8">
<title>Bright Path Fund Stationery</title>
<link href="https://fonts.googleapis.com/css2?family=Open+Sans:wght@400;600;700;800&display=swap" rel="stylesheet">
<style>
:root{
  --red:#d0202e;
  --red-dark:#a8141f;
  --ink:#2b2b2b;
  --grey:#7a7a7a;
  --line:#c9c9c9;
  --paper:#ffffff;
  --bg:#ededed;
  --mark:#f3d6d8;
}
*{margin:0;padding:0;box-sizing:border-box}
html,body{width:1200px;height:552px;overflow:hidden;background:var(--bg);font-family:"Open Sans",Arial,sans-serif;color:var(--ink)}
.canvas{position:relative;width:1200px;height:552px}
.sheet{position:absolute;background:var(--paper);box-shadow:0 1px 4px rgba(0,0,0,.18);overflow:hidden}
.fax-sheet{left:10px;top:10px;width:384px;height:523px}
.letter-sheet{left:408px;top:10px;width:384px;height:523px}
.card-front{left:811px;top:10px;width:185px;height:112px}
.card-back{left:1008px;top:10px;width:185px;height:112px;background:var(--red)}
.envelope-front{left:811px;top:139px;width:382px;height:221px}
.envelope-back{left:811px;top:379px;width:382px;height:154px}

.brand{position:absolute;display:flex;align-items:center;gap:5px}
.brand-dot{width:22px;height:22px;border-radius:50%;background:var(--red);flex:none}
.brand-name{font-weight:800;color:var(--red);font-size:15px;line-height:1;letter-spacing:-.2px}
.faint-mark{position:absolute;border-radius:50%;background:var(--mark);opacity:.45}

.footer-wave{position:absolute;left:0;bottom:0;width:100%}

.fax-title{position:absolute;right:18px;top:24px;font-weight:700;font-size:8px;letter-spacing:1px;color:var(--ink)}
.fax-form{position:absolute;left:18px;top:58px;width:348px;border-collapse:collapse;font-size:5.5px}
.fax-form td{border:1px solid var(--line);height:13px;padding:0 3px}
.fax-form .label{width:38px;font-weight:600}
.fax-options{position:absolute;left:18px;top:134px;display:flex;gap:22px;font-size:5.5px}
.fax-options span{display:flex;align-items:center;gap:3px}
.fax-options i{width:6px;height:6px;border:1px solid var(--ink);display:inline-block}

.body-copy{position:absolute;left:18px;width:348px;font-size:5.2px;line-height:1.6;color:#444;text-align:justify}
.body-copy p{margin-bottom:6px}
.sign-off{position:absolute;left:18px;font-size:5.5px;line-height:1.6}
.signature{position:absolute;left:18px;width:60px;height:14px;background:linear-gradient(90deg,#e4e4ee,#f4f4f8);border-radius:2px}
.stamp{position:absolute;width:30px;height:30px;border-radius:50%;background:#e7e3f1}

.contact-block{position:absolute;right:18px;top:16px;font-size:5px;line-height:1.6;color:var(--grey);text-align:right}
.recipient{position:absolute;left:18px;top:56px;font-size:5.5px;line-height:1.6}
.greeting{position:absolute;left:18px;top:92px;font-size:5.5px}

.card-back .card-name{position:absolute;left:12px;top:12px;color:#fff;font-size:7px;font-weight:700}
.card-back .card-role{position:absolute;left:12px;top:22px;color:#fff;font-size:4.6px}
.card-back .card-details{position:absolute;left:12px;top:40px;color:#fff;font-size:4.6px;line-height:1.7}

.env-return{position:absolute;left:16px;top:44px;font-size:5px;line-height:1.6;color:var(--grey)}
</style>
</head>
<body>
<div class="canvas">

  <section class="sheet fax-sheet">
    <div class="faint-mark" style="left:180px;top:300px;width:110px;height:110px"></div>
    <div class="brand" style="left:18px;top:14px"><span class="brand-dot"></span><span class="brand-name">Bright Path Fund</span></div>
    <div class="fax-title">FAX</div>
    <table class="fax-form">
      <tr><td class="label">To:</td><td></td><td class="label">From:</td><td></td></tr>
      <tr><td class="label">Fax:</td><td></td><td class="label">Pages:</td><td></td></tr>
      <tr><td class="label">Phone:</td><td></td><td class="label">Date:</td><td></td></tr>
      <tr><td class="label">Re:</td><td colspan="3"></td></tr>
    </table>
    <div class="fax-options">
      <span><i></i>Urgent</span><span><i></i>For Review</span><span><i></i>Please Comment</span><span><i></i>Please Reply</span><span><i></i>Please Recycle</span>
    </div>
    <div class="body-copy" style="top:152px">
      <p>Thank you for standing with our families this season. Your steady support helps us fund research, cover travel for treatment and keep hope close for every child we serve. We are grateful for each gift, large or small, and for the time you give to our cause throughout the year.</p>
      <p>This year our volunteers reached more homes than ever before. We opened two new support rooms, hosted a spring walk and raised funds for three new grants that will begin next month. Each step was made possible by friends like you who believe in our work.</p>
      <p>Our team is now planning the autumn events and a new program for parents. We will share the details with you soon, along with a full report of what your support has made possible this year.</p>
      <p>Please reach out if you have any questions about this note or our work. We look forward to sharing more good news with you soon and thank you again for your kindness.</p>
    </div>
    <div class="sign-off" style="top:404px">Yours Sincerely,</div>
    <div class="signature" role="img" aria-label="Handwritten signature" style="top:418px"></div>
    <div class="stamp" role="img" aria-label="Official seal" style="left:100px;top:410px"></div>
    <div class="sign-off" style="top:436px;font-weight:600">Dale Meridew</div>
    <svg class="footer-wave" width="384" height="44" viewBox="0 0 384 44" aria-hidden="true">
      <path d="M0 20 Q190 -4 384 14 L384 44 L0 44Z" fill="var(--red)"/>
      <path d="M0 14 Q190 -10 384 8" fill="none" stroke="var(--line)" stroke-width="1.2"/>
      <text x="192" y="36" fill="#fff" font-size="5" text-anchor="middle" font-family="Open Sans, sans-serif">20573 Lindale Avenue #238 · Helotes, Texas 78154 · www.brightpathfund.org</text>
    </svg>
  </section>

  <section class="sheet letter-sheet">
    <div class="faint-mark" style="left:150px;top:250px;width:120px;height:120px"></div>
    <div class="brand" style="left:18px;top:14px"><span class="brand-dot"></span><span class="brand-name">Bright Path Fund</span></div>
    <div class="contact-block">20573 Lindale Avenue #238<br>Helotes, Texas 78154<br>dale.meridew@brightpathfund.org<br>www.brightpathfund.org</div>
    <div class="recipient">Recipient Name<br>Street Address<br>City, State 00000</div>
    <div class="greeting">Dear Friend,</div>
    <div class="body-copy" style="top:108px">
      <p>Thank you for standing with our families this season. Your steady support helps us fund research, cover travel for treatment and keep hope close for every child we serve. We are grateful for each gift, large or small, and for the time you give to our cause throughout the year.</p>
      <p>This year our volunteers reached more homes than ever before. We opened two new support rooms, hosted a spring walk and raised funds for three new grants that will begin next month. Each step was made possible by friends like you who believe in our work.</p>
      <p>Our team is now planning the autumn events and a new program for parents. We will share the details with you soon, along with a full report of what your support has made possible this year.</p>
      <p>Families tell us that a call, a meal or a ride to the clinic can change a hard week. Your help lets us say yes to more of these requests, and it reminds every family that they do not walk alone.</p>
      <p>Please reach out if you have any questions about this letter or our work. We look forward to sharing more good news with you soon and thank you again for your kindness.</p>
    </div>
    <div class="sign-off" style="top:404px">Yours Sincerely,</div>
    <div class="signature" role="img" aria-label="Handwritten signature" style="top:418px"></div>
    <div class="sign-off" style="top:436px;font-weight:600">Dale Meridew</div>
    <svg class="footer-wave" width="384" height="44" viewBox="0 0 384 44" aria-hidden="true">
      <path d="M0 20 Q190 -4 384 14 L384 44 L0 44Z" fill="var(--red)"/>
      <path d="M0 14 Q190 -10 384 8" fill="none" stroke="var(--line)" stroke-width="1.2"/>
    </svg>
  </section>

  <section class="sheet card-front">
    <div class="brand" style="left:34px;top:34px"><span class="brand-dot" style="width:20px;height:20px"></span><span class="brand-name" style="font-size:13px">Bright Path Fund</span></div>
    <svg class="footer-wave" width="185" height="22" viewBox="0 0 185 22" aria-hidden="true">
      <path d="M0 12 Q92 -2 185 8 L185 22 L0 22Z" fill="var(--red)"/>
    </svg>
  </section>

  <section class="sheet card-back">
    <div class="card-name">Dale Meridew</div>
    <div class="card-role">President and Chairman of the Board</div>
    <div class="card-details">20573 Lindale Avenue #238<br>Helotes, Texas 78154<br>dale.meridew@brightpathfund.org<br>www.brightpathfund.org</div>
    <svg class="footer-wave" width="185" height="22" viewBox="0 0 185 22" aria-hidden="true">
      <path d="M0 12 Q92 -2 185 8 L185 22 L0 22Z" fill="#fff"/>
    </svg>
  </section>

  <section class="sheet envelope-front">
    <div class="faint-mark" style="left:230px;top:40px;width:120px;height:120px"></div>
    <div class="brand" style="left:16px;top:14px"><span class="brand-dot"></span><span class="brand-name">Bright Path Fund</span></div>
    <div class="env-return">20573 Lindale Avenue #238<br>Helotes, Texas 78154</div>
    <svg class="footer-wave" width="382" height="34" viewBox="0 0 382 34" aria-hidden="true">
      <path d="M0 16 Q190 -4 382 12 L382 34 L0 34Z" fill="var(--red)"/>
    </svg>
  </section>

  <section class="sheet envelope-back">
    <svg width="382" height="154" viewBox="0 0 382 154" aria-hidden="true">
      <path d="M0 0 L382 0 L382 40 L191 96 L0 40Z" fill="var(--red)"/>
      <path d="M0 40 L191 96 L382 40" fill="none" stroke="var(--red-dark)" stroke-width="1"/>
    </svg>
  </section>

</div>
</body>
</html>
```